Flyer for Lawnmowing and gardening business

We are a lawn mowing and gardening business needing a flyer designed listing our services and business info.
The flyer should include all business information and contact details as below.

Lawn mowing
Gardening
Green waste removal
Pruning
Weeding
Vegetable Garden Creation

Phone number:0457302864

As well as the logo provided

Target Market(s)

Local people wanting someone to care for their garden.

Industry/Entity Type

Gardener

Font styles to use
Serif

Requirements
Must have
• Business Logo
• All business info and services provided. EG
• Lawn mowing
• Gardening
• Green waste removal
• Pruning
• Weeding
• Vegetable Garden Creation
• Phone number:0457302864
Nice to have
• Earthy tones, clean and simple flyer design

```html
<!DOCTYPE html>
<html lang="en">
<head>
<meta charset="utf-8">
<title>Verdant Edge – Lawn Mowing & Garden Care Flyer</title>
<link href="https://fonts.googleapis.com/css2?family=Anton&family=Oswald:wght@300;400;500&display=swap" rel="stylesheet">
<style>
  :root {
    --deep-green: #0d2a12;
    --grass: #5f8f2a;
    --lime-pale: #cde87a;
    --lawn-green: #52d452;
    --gardening-lime: #c9f03b;
    --green-lime: #9fe33a;
    --pruning-yellow: #f4e01c;
    --weeding-cyan: #3fe3e0;
    --white: #ffffff;
    --ink: #2b3a22;
  }
  * { box-sizing: border-box; margin: 0; padding: 0; }
  html, body { width: 1200px; height: 2536px; overflow: hidden; background: var(--white); }
  .flyer { position: relative; width: 1200px; height: 2536px; overflow: hidden; background: var(--white); font-family: "Oswald", sans-serif; }
  .backdrop { position: absolute; inset: 0; width: 1200px; height: 2536px; }

  .phone-label {
    position: absolute; top: 26px; left: 560px;
    font-family: "Oswald", sans-serif; font-weight: 300; font-size: 54px;
    color: var(--white); letter-spacing: 5px; line-height: 1;
  }
  .phone-tab {
    position: absolute; top: 88px; right: 0; width: 752px; height: 120px;
    background: var(--lime-pale); border-radius: 60px 0 0 60px;
    display: flex; align-items: center; padding-left: 100px;
  }
  .phone-number {
    font-family: "Oswald", sans-serif; font-weight: 400; font-size: 110px;
    color: var(--deep-green); letter-spacing: 3px; line-height: 1;
  }

  .services { position: absolute; inset: 0; list-style: none; }
  .line {
    position: absolute; left: 72px; display: block; white-space: nowrap; line-height: 1;
    text-transform: uppercase; transform-origin: left top; transform: scaleX(var(--stretch, 1));
  }
  .line--main { font-family: "Anton", sans-serif; }
  .line--sub { font-family: "Oswald", sans-serif; font-weight: 300; }

  .lawn { color: var(--lawn-green); }
  .gardening { color: var(--gardening-lime); }
  .green { color: var(--green-lime); }
  .pruning { color: var(--pruning-yellow); }
  .weeding { color: var(--weeding-cyan); }
  .vegetable { color: var(--white); }

  .lawn .line--main { top: 70px; font-size: 126px; }
  .lawn .line--sub { top: 192px; font-size: 86px; --stretch: 1.15; }
  .gardening .line--main { top: 318px; font-size: 135px; --stretch: 1.08; }
  .green .line--main { top: 470px; font-size: 112px; --stretch: 1.3; }
  .green .line--sub { top: 584px; font-size: 84px; --stretch: 1.1; }
  .pruning .line--main { top: 708px; font-size: 144px; --stretch: 1.3; }
  .weeding .line--main { top: 880px; font-size: 126px; --stretch: 1.3; }
  .vegetable .line--main { top: 1028px; font-size: 135px; --stretch: 1.15; }
  .vegetable .line--sub { top: 1160px; font-size: 96px; font-weight: 400; }

  .brand {
    position: absolute; left: 300px; right: 20px; top: 2150px;
    display: flex; flex-direction: column; align-items: center;
  }
  .brand-dot { width: 120px; height: 120px; border-radius: 50%; background: var(--grass); margin-bottom: 50px; }
  .brand-name {
    font-family: "Oswald", sans-serif; font-weight: 500; font-size: 104px;
    color: var(--ink); text-transform: uppercase; letter-spacing: 6px; line-height: 1;
  }
  .brand-tagline {
    margin-top: 14px;
    font-family: "Oswald", sans-serif; font-weight: 400; font-size: 58px;
    color: var(--ink); text-transform: uppercase; letter-spacing: 4px; line-height: 1;
  }
</style>
</head>
<body>
<div class="flyer">
  <svg class="backdrop" viewBox="0 0 1200 2536" xmlns="http://www.w3.org/2000/svg">
    <defs>
      <radialGradient id="lawnSpray" cx="0.75" cy="0.3" r="0.9">
        <stop offset="0" stop-color="#6f7f66"/>
        <stop offset="0.45" stop-color="#2f4a22"/>
        <stop offset="1" stop-color="#0c1f0c"/>
      </radialGradient>
      <linearGradient id="seedling" x1="0" y1="0" x2="1" y2="1">
        <stop offset="0" stop-color="#b8d98a"/>
        <stop offset="0.45" stop-color="#5f8f2a"/>
        <stop offset="0.8" stop-color="#6a4a2a"/>
        <stop offset="1" stop-color="#3a2a18"/>
      </linearGradient>
      <linearGradient id="bandGreen" x1="0" y1="0" x2="1" y2="0">
        <stop offset="0" stop-color="#7fbf2a"/>
        <stop offset="1" stop-color="#d4ea8a"/>
      </linearGradient>
    </defs>
    <g role="img" aria-label="Photo of a sprinkler spraying water over a green lawn">
      <polygon points="0,0 1200,0 1200,1100 0,1440" fill="url(#lawnSpray)"/>
    </g>
    <g role="img" aria-label="Photo of a young seedling in a terracotta pot beside a garden fork in soil">
      <polygon points="0,1440 1200,1100 1200,1880 0,2180" fill="url(#seedling)"/>
    </g>
    <polygon points="0,1420 1200,1075 1200,1130 0,1480" fill="url(#bandGreen)"/>
    <polygon points="0,2160 1200,1850 1200,1900 0,2220" fill="url(#bandGreen)"/>
    <polygon points="0,2220 1200,1900 1200,2536 0,2536" fill="#ffffff"/>
  </svg>

  <div class="phone-label">PHONE NO.</div>
  <div class="phone-tab"><span class="phone-number">0457302864</span></div>

  <ul class="services">
    <li class="lawn"><span class="line line--main">Lawn</span><span class="line line--sub">Mowing</span></li>
    <li class="gardening"><span class="line line--main">Gardening</span></li>
    <li class="green"><span class="line line--main">Green</span><span class="line line--sub">Waste Removal</span></li>
    <li class="pruning"><span class="line line--main">Pruning</span></li>
    <li class="weeding"><span class="line line--main">Weeding</span></li>
    <li class="vegetable"><span class="line line--main">Vegetable</span><span class="line line--sub">Gardencreation</span></li>
  </ul>

  <div class="brand">
    <div class="brand-dot"></div>
    <div class="brand-name">Verdant Edge</div>
    <div class="brand-tagline">Lawn Mowing &amp; Garden Care</div>
  </div>
</div>
</body>
</html>
```